Web Design Project for new Anaesthetic Pracitice

We have recently obtained our brand new logo from PixelHarbor and now it's time to move on to our website. We are a new anaesthetic practice that offers state of the art anaesthesia care.

We are after a design that communicates professionalism, along with a modern, forward thinking attitude.

Reason: I would like the chance to see more designs. I have also increased the budget and will be providing a little more guidance on required elements.

I have just increased the budget on this project.  $400 for first place, $100 for second.

Also view the brief for some further guidance to help refine designs

Reason: As our deadline is now almost upon us and we have only just sorted out the issues with our increased budget I thought it only fair to give other designers a chance to see if they wish to participate. As a consolation to you all the project is now guaranteed.

Target Market(s)

Our patients and to a lesser extent the surgeons we work with

Requirements
Must have
• The same clean, sleek modern look that we have in our logo. The logo should feature prominently (examples are uploaded)

Menu system, either vertical or horizontal.
The menu system will include the following:
• Home
• Our People
• Our Hospitals
• Our Charges
• Booking Form
• Patient Information
• Contact Information

If designers think they can find more succinct wording for these categories they are free to try.

Some of these menu entries will in all probability lead to a drop down menu (Or People, Our Hospitals and Patient Information in particular). Consideration to how these menus will look and what they are likely to cover is a must.

If your design is selected you will be asked to produce a PSD for both the main page and for any secondary pages (which will be a development of the main page, with the same basic layout, just with a single lot of content) unless your design is one where all pages on the site look the same (i.e. the main page does not have portions of the other pages or leaders on it)

Design delivered as a layered PSD file so we can have our coders chop and slice it into a CSS website.

Use of the logo as uploaded below

A space reserved for breadcrumbs.

Use of the VaultMark logo, preferably in the footer, but we will accept it at the bottom of a side bar. Examples are included below.

The font in the logo is Sommet. We have the ability to install this as a webfont, feel free to utilise it in the site if you so wish.

Contact information can be either a menu option or in the footer.

Nice to have
• Rotating images (either provide us with dummies or just blank placeholder spaces, we have an in-house professional photographer who will be able to populate any such area)

Either a design with all pages on the site looking the same or with a main home page and a separate, related design for other pages (the full site will have about 30 pages, covering how to get to the office, how to get to the hospitals we work at (with wayfind atlas), the doctors working for us, our office staff, some information on why we charge what we do, and a range of patient information pages)

Icons for Chatterly and Quibbler. We have no need for Vid Nest, Plok, Snapra or Murmur right now, but if you want to include icons for these, feel free, we can always use them later.

These sort of icons can be placed anywhere but personally I like them in the footer.

A footer menu is not mandatory but if it works better with your design feel free to do so.
Should not have
• Pictures of young doctors in white coats, stethoscopes, cadeucus (staff and serpent), all are clichéd and worn out.

```html
<!DOCTYPE html>
<html lang="en">
<head>
<meta charset="utf-8">
<title>Loddon Ridge Anaesthetic Specialists</title>
<link rel="stylesheet" href="https://fonts.googleapis.com/css2?family=Roboto:wght@400;500;700&display=swap">
<style>
:root{
  --red:#d8232f;
  --red-dark:#b8141f;
  --red-text:#d22630;
  --ink:#1d1d1d;
  --page:#efefef;
  --page-light:#f7f7f7;
  --white:#ffffff;
  --footer:#111111;
  --footer-link:#8b8b8b;
  --line:#d6d6d6;
  --field-text:#9a9a9a;
}
*{box-sizing:border-box;margin:0;padding:0}
html,body{width:916px;height:1200px;overflow:hidden}
body{font-family:"Roboto",Arial,sans-serif;color:var(--ink);background:var(--page);position:relative}
.abs{position:absolute}

/* header */
.top-rule{left:0;top:0;width:916px;height:4px;background:#111}
.header-band{left:0;top:4px;width:916px;height:396px;background:var(--red)}
.page-body{left:0;top:400px;width:916px;height:630px;background:radial-gradient(ellipse at 50% 40%,var(--page-light) 0%,var(--page) 70%,#e2e2e2 100%)}
.breadcrumb{left:649px;top:0;width:175px;height:22px;background:#111;border-radius:0 0 3px 3px;color:#bdbdbd;font-size:9px;line-height:22px;padding-left:8px;white-space:nowrap}
.brand{left:92px;top:18px;display:flex;align-items:center;gap:10px}
.brand-dot{width:46px;height:46px;border-radius:50%;background:var(--red-dark)}
.brand-name{color:var(--white);font-weight:500;font-size:15px;line-height:19px}
.main-nav{right:92px;top:49px;display:flex;font-size:11px;white-space:nowrap}
.main-nav a{color:var(--white);text-decoration:none;height:20px;line-height:20px;padding:0 6px}
.main-nav a.current{background:#e84a52;border-radius:2px;font-weight:700;padding:0 12px;margin-right:2px}

/* slider */
.slider-frame{left:90px;top:85px;width:734px;height:341px;background:var(--white);border-radius:3px;box-shadow:0 2px 3px rgba(0,0,0,.25)}
.slider-photo{left:94px;top:89px;width:726px;height:332px;background:radial-gradient(ellipse at 60% 50%,#5c7fa8 0%,#2d4b72 35%,#15243d 75%,#0c1628 100%)}
.slide-arrow{top:214px;width:18px;height:52px;background:var(--page-light)}
.slide-arrow.left{left:94px;border-radius:0 26px 26px 0}
.slide-arrow.right{left:802px;border-radius:26px 0 0 26px}
.slide-arrow svg{position:absolute;top:20px}
.slide-copy{left:138px;top:222px;color:var(--white);width:250px}
.slide-copy h1{font-weight:400;font-size:21px;margin-bottom:10px}
.slide-copy p{font-size:9.6px;line-height:12px;margin-bottom:12px}
.btn{display:inline-block;background:linear-gradient(#e8414b,var(--red-dark));color:var(--white);font-size:9.5px;text-align:center;border-radius:2px;box-shadow:0 2px 0 #8d1118;line-height:18px;height:18px}
.slide-copy .btn{width:76px}
.pager{left:418px;top:400px;width:72px;height:21px;background:var(--white);border-radius:12px 12px 0 0;display:flex;justify-content:center;gap:7px;padding-top:8px}
.pager span{width:7px;height:7px;border-radius:50%;background:#bbb}
.pager span:first-child{background:#888}
.slider-shadow{left:60px;top:428px;width:796px;height:18px;background:radial-gradient(ellipse at 50% 0,rgba(0,0,0,.28) 0%,rgba(0,0,0,0) 70%)}

/* features */
.feature{top:466px;width:170px;text-align:center}
.feature .icon{height:50px;display:flex;justify-content:center;align-items:center;margin-bottom:22px}
.feature h2{color:var(--red-text);font-weight:400;font-size:15px;margin-bottom:9px}
.feature p{text-align:left;font-size:9.6px;line-height:12px;height:84px}
.feature .btn{width:76px}
.globe{width:48px;height:48px;border-radius:50%;background:radial-gradient(circle at 35% 35%,#b6dcff 0%,#4a8fd6 45%,#1f5aa3 100%)}
.divider{left:100px;top:691px;width:716px;height:1px;background:linear-gradient(90deg,transparent,var(--line) 15%,var(--line) 85%,transparent)}

/* content */
.section-title{color:var(--red-text);font-weight:400;font-size:15.5px}
.copy{font-size:9.6px;line-height:12px}
.welcome{left:99px;top:729px;width:350px}
.welcome .copy{margin-top:10px}
.welcome .copy + .copy{margin-top:12px}
.welcome .second{margin-top:30px}
.news{left:466px;top:729px;width:170px}
.news .copy{margin-top:10px}
.news .item + .item{margin-top:24px}
.news .btn{width:76px;margin-top:6px}
.contact{left:649px;top:729px;width:168px}
.contact .copy{margin-top:10px;margin-bottom:5px}
.field{width:168px;height:20px;background:var(--white);border:1px solid #ddd;border-radius:2px;font-size:9.5px;color:var(--field-text);line-height:18px;padding-left:6px;margin-top:5px}
.field.select{background:linear-gradient(#fafafa,#e4e4e4);position:relative}
.field.select svg{position:absolute;right:5px;top:7px}
.field.message{height:81px}
.contact .btn{width:168px;margin-top:7px}

/* footer */
.site-footer{left:0;top:1030px;width:916px;height:170px;background:var(--footer)}
.foot-col{top:1055px}
.foot-col h3{color:var(--white);font-size:12px;font-weight:700;margin-bottom:11px}
.foot-col li{list-style:none;color:var(--footer-link);font-size:9px;line-height:19.2px}
.social{width:75px;height:24px;background:#222;border:1px solid #333;border-radius:2px;display:flex;align-items:center;gap:7px;padding-left:2px;color:var(--white);font-size:8.5px;font-weight:500}
.social i{width:19px;height:19px;display:block}
</style>
</head>
<body>
<div class="abs top-rule"></div>
<div class="abs header-band"></div>
<div class="abs page-body"></div>

<div class="abs breadcrumb">Services &gt; anesthetics &gt; Class1</div>

<div class="abs brand">
  <span class="brand-dot"></span>
  <span class="brand-name">Loddon Ridge<br>Anaesthetic Specialists</span>
</div>

<nav class="abs main-nav">
  <a class="current">Home</a><a>Our People</a><a>Hospitals</a><a>Charges</a><a>Booking</a><a>Patient Info</a><a>Contact</a>
</nav>

<div class="abs slider-frame"></div>
<div class="abs slider-photo" role="img" aria-label="Slide photo: glowing blue neuron network"></div>
<div class="abs slide-arrow left"><svg width="10" height="10" style="left:2px"><path d="M7 1 L2 5 L7 9Z" fill="#bbb"/></svg></div>
<div class="abs slide-arrow right"><svg width="10" height="10" style="left:6px"><path d="M3 1 L8 5 L3 9Z" fill="#bbb"/></svg></div>
<div class="abs slide-copy">
  <h1>Your Tagline Goes Here</h1>
  <p>This is Canvasly's version of Lorem Ipsum. Proin gravida nibh vel velit auctor aliquet.</p>
  <span class="btn">learn more</span>
</div>
<div class="abs pager"><span></span><span></span><span></span><span></span><span></span></div>
<div class="abs slider-shadow"></div>

<section class="abs feature" style="left:99px">
  <div class="icon"><div class="globe" role="img" aria-label="Globe icon"></div></div>
  <h2>Satisfied Clients</h2>
  <p>This is Canvasly's version of Lorem Ipsum. Proin gravida nibh vel velit auctor aliquet. Aenean sollicitudin, lorem quis bibendum auctor, nisi elit consequat ipsum, nec sagittis sem nibh id elit.</p>
  <span class="btn">read more</span>
</section>
<section class="abs feature" style="left:282px">
  <div class="icon"><svg width="48" height="48" viewBox="0 0 48 48"><path d="M3 28 L10 22 L19 33 L44 3 L47 6 L19 44Z" fill="#8cc63f"/></svg></div>
  <h2>24x7 Support</h2>
  <p>This is Canvasly's version of Lorem Ipsum. Proin gravida nibh vel velit auctor aliquet. Aenean sollicitudin, lorem quis bibendum auctor, nisi elit consequat ipsum, nec sagittis sem nibh id elit.</p>
  <span class="btn">read more</span>
</section>
<section class="abs feature" style="left:466px">
  <div class="icon"><svg width="48" height="48" viewBox="0 0 48 48"><circle cx="24" cy="24" r="22" fill="#6a9ad8"/><circle cx="24" cy="24" r="18" fill="#f4f4f4"/><path d="M24 10 V24 H34" stroke="#222" stroke-width="2" fill="none"/><circle cx="24" cy="24" r="2" fill="#222"/></svg></div>
  <h2>Timed Delivery</h2>
  <p>This is Canvasly's version of Lorem Ipsum. Proin gravida nibh vel velit auctor aliquet. Aenean sollicitudin, lorem quis bibendum auctor, nisi elit consequat ipsum, nec sagittis sem nibh id elit.</p>
  <span class="btn">read more</span>
</section>
<section class="abs feature" style="left:649px">
  <div class="icon"><svg width="48" height="48" viewBox="0 0 48 48"><g fill="#9ea5a8"><rect x="20" y="1" width="8" height="46" rx="2"/><rect x="20" y="1" width="8" height="46" rx="2" transform="rotate(45 24 24)"/><rect x="20" y="1" width="8" height="46" rx="2" transform="rotate(90 24 24)"/><rect x="20" y="1" width="8" height="46" rx="2" transform="rotate(135 24 24)"/><circle cx="24" cy="24" r="17"/></g><circle cx="24" cy="24" r="7" fill="var(--page)"/></svg></div>
  <h2>Unmatched Quality</h2>
  <p>This is Canvasly's version of Lorem Ipsum. Proin gravida nibh vel velit auctor aliquet. Aenean sollicitudin, lorem quis bibendum auctor, nisi elit consequat ipsum, nec sagittis sem nibh id elit.</p>
  <span class="btn">read more</span>
</section>

<div class="abs divider"></div>

<section class="abs welcome">
  <h2 class="section-title">Welcome to Loddon Ridge</h2>
  <p class="copy">This is Canvasly's version of Lorem Ipsum. Proin gravida nibh vel velit auctor aliquet. Aenean sollicitudin, lorem quis bibendum auctor, nisi elit consequat ipsum, nec sagittis sem nibh id elit. Duis sed odio sit amet nibh vulputate cursus a sit amet mauris.</p>
  <p class="copy">Morbi accumsan ipsum velit. Nam nec tellus a odio tincidunt auctor a ornare odio. Sed non mauris vitae erat consequat auctor eu in elit.</p>
  <h2 class="section-title second">Anesthetic Specialists</h2>
  <p class="copy">This is Canvasly's version of Lorem Ipsum. Proin gravida nibh vel velit auctor aliquet. Aenean sollicitudin, lorem quis bibendum auctor, nisi elit consequat ipsum, nec sagittis sem nibh id elit. Duis sed odio sit amet nibh vulputate cursus a sit amet mauris.</p>
  <p class="copy">Morbi accumsan ipsum velit. Nam nec tellus a odio tincidunt auctor a ornare odio. Sed non mauris vitae erat consequat auctor eu in elit.</p>
</section>

<section class="abs news">
  <h2 class="section-title">Latest News</h2>
  <div class="item"><p class="copy">This is Canvasly's version of Lorem Ipsum. Proin gravida nibh vel velit auctor aliquet.</p><span class="btn">read more</span></div>
  <div class="item"><p class="copy">This is Canvasly's version of Lorem Ipsum. Proin gravida nibh vel velit auctor aliquet.</p><span class="btn">read more</span></div>
  <div class="item"><p class="copy">This is Canvasly's version of Lorem Ipsum. Proin gravida nibh vel velit auctor aliquet.</p><span class="btn">read more</span></div>
</section>

<section class="abs contact">
  <h2 class="section-title">Contact Us</h2>
  <p class="copy">Fill the contact form below and our representatives will call you within 24 hours !!</p>
  <div class="field">Name</div>
  <div class="field">Email Address</div>
  <div class="field select">Select Service Type<svg width="6" height="4"><path d="M0 0H6L3 4Z" fill="#444"/></svg></div>
  <div class="field message">Message</div>
  <span class="btn">Hear from Us</span>
</section>

<footer class="abs site-footer"></footer>
<div class="abs foot-col" style="left:99px"><h3>INFORMATION</h3><ul><li>Contact</li><li>Delivery</li><li>Legal Notice</li><li>Terms and Conditions</li><li>About Us</li></ul></div>
<div class="abs foot-col" style="left:239px"><h3>Downloads</h3><ul><li>Contact</li><li>Delivery</li><li>Legal Notice</li><li>Terms and Conditions</li><li>About Us</li></ul></div>
<div class="abs foot-col" style="left:380px"><h3>Help</h3><ul><li>Contact</li><li>Delivery</li><li>Legal Notice</li><li>Terms and Conditions</li><li>About Us</li></ul></div>
<div class="abs foot-col" style="left:519px"><h3>About Us</h3><ul><li>Contact</li><li>Delivery</li><li>Legal Notice</li><li>Terms and Conditions</li><li>About Us</li></ul></div>

<div class="abs social" style="left:649px;top:1058px"><i style="background:#0e76a8"></i>Linkwork</div>
<div class="abs social" style="left:742px;top:1058px"><i style="background:#c8322a"></i>Orbita +</div>
<div class="abs social" style="left:649px;top:1088px"><i style="background:#3b5998"></i>Chatterly</div>
<div class="abs social" style="left:742px;top:1088px"><i style="background:#b7121d"></i>Pinboardy</div>
<div class="abs social" style="left:649px;top:1118px"><i style="background:#2aa6e0"></i>Quibbler</div>
<div class="abs social" style="left:742px;top:1118px"><i style="background:#ef7a1a"></i>RSS feed</div>
</body>
</html>
```